"Ride the amber tide" fitness and nutrition website/blog/forum

We need a website design for a gym training/nutrition website/blog. It is going to eventually have articles aimed at both men and women and will have content about exercise, nutrition, and the science behind both.

I want to have:
a home page
a page for all articles/blog posts about Nutrition
a page for all articles/blog posts about Training
a page where we can share articles about workouts targeting different muscle groups
a forum, where people can discuss nutrition and training (I would want this to be fairly simple to use and control as I am not a coder/programmer)

Design wise, I would like to use high contrast colours, such as black and white, but definitely open to some sort of colour theme, maybe some blue, or red, or purple, I am not sure, I would have to see an example.

We will be monetising this site with adverts, so there needs to be some space built in for this in the theme, however we don't want this to be overbearing, I don't want this to look like a spam site.

We have a logo, I have attached this. I haven't written any content for the homepage yet, as I wanted the design first before I worked out what to write and where to put it.

We will have social media accounts on instagram, twitter and facebook so would like buttons on the header and footer for these.

Target Market(s)

Fitness enthusiasts

Industry/Entity Type

fitness

Coding

Coded - Design and coding required

Number of Pages Required

5+ page

Font styles to use
Serif
Sans Serif

Colors

Designer to choose colors to be used in the design.

Requirements
Must have
• Space for some ads, a forum area, a page for nutrition blog posts, a page for training posts, a page for workout posts.

```html
<!DOCTYPE html>
<html lang="en">
<head>
<meta charset="utf-8">
<title>Ride the amber tide – Nutrition</title>
<link href="https://fonts.googleapis.com/css2?family=Jost:wght@400;500&family=Mulish:wght@400;500;600&display=swap" rel="stylesheet">
<style>
:root{
  --ink:#1b1b1b;
  --text:#2a2a2a;
  --blue:#14549a;
  --red:#e8202a;
  --band:#e6e8ec;
  --card:#f4f4f4;
  --rule:#dcdcdc;
  --dark-dot:#3a3a3a;
}
*{margin:0;padding:0;box-sizing:border-box}
html,body{width:1200px;height:2227px;overflow:hidden;background:#fff}
body{position:relative;font-family:"Mulish",sans-serif;color:var(--text)}
.abs{position:absolute}

/* header */
.site-header{position:absolute;left:0;top:0;width:1200px;height:156px;background:var(--band);border-bottom:1px solid #222}
.brand{position:absolute;display:flex;align-items:center;gap:8px;font-family:"Jost",sans-serif;font-weight:500;color:var(--ink)}
.brand-dot{width:14px;height:14px;border-radius:50%;background:var(--ink);flex:none}
.header-brand{left:151px;top:62px;font-size:19px}
.get-social{position:absolute;left:730px;top:49px;display:flex;align-items:center;gap:8px;font-size:11px;font-weight:600;letter-spacing:.6px;color:var(--blue)}
.get-social .label{margin-right:6px}
.dot{width:20px;height:20px;border-radius:50%;background:var(--dark-dot);display:block}
.dot.blue{background:var(--blue)}
.login{position:absolute;left:933px;top:40px;width:112px;height:34px;background:var(--red);color:#fff;font-size:11.5px;font-weight:600;letter-spacing:.8px;display:flex;align-items:center;justify-content:center;gap:6px}
.main-nav{position:absolute;left:396px;top:110px;width:651px;display:flex;justify-content:space-between;font-family:"Jost",sans-serif;font-size:12.5px;letter-spacing:1px;color:var(--ink)}
.main-nav .active{color:var(--red)}

/* article */
.hero{left:230px;top:236px;width:740px;height:322px;background:linear-gradient(120deg,#7a5a3c 0%,#8fa6b4 40%,#6f8c4a 60%,#9a7650 100%)}
.date{display:flex;align-items:center;gap:7px;font-family:"Jost",sans-serif;font-size:14.5px;color:var(--blue)}
.date sup{font-size:7px}
.article-date{left:230px;top:592px}
.article-title{left:230px;top:621px;width:440px;font-family:"Jost",sans-serif;font-weight:400;font-size:23.5px;line-height:30px;color:var(--ink)}
.body-copy{left:230px;width:742px;font-size:12.2px;letter-spacing:.15px;line-height:19.4px;color:var(--text)}
.sub{left:230px;font-family:"Jost",sans-serif;font-weight:400;font-size:17px;color:var(--ink)}
.ticks{left:230px;top:848px;list-style:none;font-size:12.2px;letter-spacing:.15px;color:var(--text)}
.ticks li{height:24px;display:flex;align-items:center;gap:16px}
.share{left:229px;top:1311px;width:742px;height:49px;border-top:1px solid var(--rule);border-bottom:1px solid var(--rule);display:flex;align-items:center;gap:12px}
.share .label{font-size:11px;font-weight:600;letter-spacing:.6px;color:var(--blue);margin-right:12px}
.share .dot{width:30px;height:30px}

/* related */
.related-title{left:0;top:1413px;width:1200px;text-align:center;font-family:"Jost",sans-serif;font-weight:500;font-size:28px;letter-spacing:1.5px;color:var(--blue)}
.related-rule{top:1435px;width:76px;height:2px;background:var(--blue)}
.card{top:1500px;width:358px;height:417px;background:var(--card)}
.card-photo{position:absolute;left:0;top:0;width:358px;height:205px}
.photo-training{background:linear-gradient(135deg,#b98360 0%,#5e4a3e 55%,#2e2e33 100%)}
.photo-workouts{background:linear-gradient(135deg,#c9b49c 0%,#7d8a96 50%,#3a3a40 100%)}
.tag{position:absolute;left:0;top:0;height:21px;padding:0 9px 0 7px;background:var(--blue);color:#fff;font-size:11px;font-weight:600;letter-spacing:.6px;display:flex;align-items:center;gap:5px}
.card-body{position:absolute;left:0;top:220px;width:358px;text-align:center}
.card-body .date{justify-content:center;font-size:13.5px}
.card-title{margin-top:6px;font-family:"Jost",sans-serif;font-weight:400;font-size:16.5px;line-height:22px;color:var(--ink)}
.card-rule{width:40px;height:1px;background:var(--blue);margin:11px auto 10px}
.card-text{font-size:11.8px;letter-spacing:.15px;line-height:18px;color:var(--text)}
.read-more{position:absolute;left:131px;top:400px;width:96px;height:26px;border:1.5px solid var(--red);background:#fff;color:var(--red);font-size:11px;font-weight:600;letter-spacing:1px;display:flex;align-items:center;justify-content:center}

/* footer */
.site-footer{position:absolute;left:0;top:2006px;width:1200px;height:221px;background:var(--band)}
.footer-brand{left:76px;top:102px;font-size:18px}
.footer-nav{position:absolute;left:329px;top:66px;width:544px;display:flex;justify-content:space-between;font-size:12.5px;letter-spacing:.8px;color:#333}
.footer-nav .home{color:var(--ink);font-weight:600}
.footer-nav .active{color:var(--red)}
.footer-rule{position:absolute;top:127px;width:205px;height:1px;background:#9aa8bf}
.footer-social{position:absolute;left:542px;top:112px;display:flex;gap:13px}
.footer-social .dot{width:30px;height:30px}
.copyright{position:absolute;left:0;top:174px;width:1200px;text-align:center;font-size:11.5px;color:var(--ink)}
.copyright span{color:var(--blue)}
.to-top{position:absolute;left:1111px;top:99px;width:24px;height:24px;background:var(--blue);transform:rotate(45deg)}
.to-top-arrow{position:absolute;left:1115px;top:103px}
</style>
</head>
<body>

<header class="site-header">
  <div class="brand header-brand"><span class="brand-dot"></span>Ride the amber tide</div>
  <div class="get-social">
    <span class="label">GET SOCIAL:</span>
    <span class="dot" aria-label="Social profile link"></span>
    <span class="dot blue" aria-label="Social profile link"></span>
    <span class="dot" aria-label="Social profile link"></span>
  </div>
  <a class="login">
    <svg width="9" height="10" viewBox="0 0 9 10"><circle cx="4.5" cy="2.6" r="2.3" fill="#fff"/><path d="M0 10c0-3 2-4.5 4.5-4.5S9 7 9 10z" fill="#fff"/></svg>
    LOGIN
  </a>
  <nav class="main-nav">
    <span>HOME</span><span>ABOUT US</span><span class="active">NUTRITION</span><span>TRAINING</span><span>WORKOUTS</span><span>FORUM</span><span>CONTACT US</span>
  </nav>
</header>

<main>
  <div class="abs hero" role="img" aria-label="Overhead photo of a healthy salad bowl with egg, tomato, avocado and radish on a wooden table"></div>

  <div class="abs date article-date">
    <svg width="14" height="13" viewBox="0 0 14 13"><rect x="1" y="2" width="12" height="10" fill="none" stroke="#14549a" stroke-width="1.5"/><rect x="1" y="2" width="12" height="3" fill="#14549a"/><rect x="3.5" y="0" width="1.5" height="3" fill="#14549a"/><rect x="9" y="0" width="1.5" height="3" fill="#14549a"/></svg>
    <span>DEC 18<sup>TH.</sup> 2022</span>
  </div>

  <h1 class="abs article-title">Contrary to popular belief, lorem Ipsum is not simply</h1>

  <p class="abs body-copy" style="top:694px">Lorem Ipsum is simply dummy text of the printing and typesetting industry. Lorem Ipsum has been the industry's standard dummy text ever since the 1500s, when an unknown printer took a galley of type and scrambled it to make a type specimen book. It has survived not only five centuries, but also the leap into electronic typesetting, remaining essentially unchanged. It was popularised in the 1960s with the release of Lettrix sheets containing Lorem Ipsum passages, and more recently with desktop publishing software like Folio Layout including versions of Lorem Ipsum.</p>

  <h2 class="abs sub" style="top:809px">Contrary to popular belief, lorem Ipsum</h2>

  <ul class="abs ticks">
    <li><svg width="13" height="8" viewBox="0 0 13 8"><path d="M1 4l2.5 3L9 1M5 5.5L6.5 7 12 1" fill="none" stroke="#14549a" stroke-width="1.1"/></svg>Lorem Ipsum is simply dummy text of the printing and typesetting industry.</li>
    <li><svg width="13" height="8" viewBox="0 0 13 8"><path d="M1 4l2.5 3L9 1M5 5.5L6.5 7 12 1" fill="none" stroke="#14549a" stroke-width="1.1"/></svg>Lorem Ipsum has been the industry's standard</li>
    <li><svg width="13" height="8" viewBox="0 0 13 8"><path d="M1 4l2.5 3L9 1M5 5.5L6.5 7 12 1" fill="none" stroke="#14549a" stroke-width="1.1"/></svg>Dummy text ever since the 1500s, when an unknown printer took a galley of type and scrambled.</li>
    <li><svg width="13" height="8" viewBox="0 0 13 8"><path d="M1 4l2.5 3L9 1M5 5.5L6.5 7 12 1" fill="none" stroke="#14549a" stroke-width="1.1"/></svg>It to make a type specimen book. It has survived not only five centuries, but also the leap into.</li>
    <li><svg width="13" height="8" viewBox="0 0 13 8"><path d="M1 4l2.5 3L9 1M5 5.5L6.5 7 12 1" fill="none" stroke="#14549a" stroke-width="1.1"/></svg>Electronic typesetting, remaining essentially unchanged.</li>
  </ul>

  <h2 class="abs sub" style="top:987px">Contrary to popular belief, lorem Ipsum</h2>
  <p class="abs body-copy" style="top:1026px">Lorem Ipsum is simply dummy text of the printing and typesetting industry. Lorem Ipsum has been the industry's standard dummy text ever since the 1500s, when an unknown printer took a galley of type and scrambled it to make a type specimen book. It has survived not only five centuries, but also the leap into electronic typesetting, remaining essentially unchanged. It was popularised in the 1960s with the release of Lettrix sheets containing Lorem Ipsum passages, and more recently with desktop publishing software like Folio Layout including versions of Lorem Ipsum.</p>

  <h2 class="abs sub" style="top:1140px">Contrary to popular belief, lorem Ipsum</h2>
  <p class="abs body-copy" style="top:1179px">Lorem Ipsum is simply dummy text of the printing and typesetting industry. Lorem Ipsum has been the industry's standard dummy text ever since the 1500s, when an unknown printer took a galley of type and scrambled it to make a type specimen book. It has survived not only five centuries, but also the leap into electronic typesetting, remaining essentially unchanged. It was popularised in the 1960s with the release of Lettrix sheets containing Lorem Ipsum passages, and more recently with desktop publishing software like Folio Layout including versions of Lorem Ipsum.</p>

  <div class="abs share">
    <span class="label">SHARE ON</span>
    <span class="dot" aria-label="Share link"></span>
    <span class="dot blue" aria-label="Share link"></span>
    <span class="dot" aria-label="Share link"></span>
  </div>

  <section>
    <span class="abs related-rule" style="left:383px"></span>
    <h2 class="abs related-title">Related Articles</h2>
    <span class="abs related-rule" style="left:741px"></span>

    <article class="abs card" style="left:230px">
      <div class="card-photo photo-training" role="img" aria-label="Group doing sit-ups on a gym floor"></div>
      <span class="tag"><svg width="9" height="9" viewBox="0 0 9 9"><path d="M4 0h5v5L4 9 0 5z" fill="#fff"/></svg>TRAINING</span>
      <div class="card-body">
        <div class="date"><svg width="13" height="12" viewBox="0 0 14 13"><rect x="1" y="2" width="12" height="10" fill="none" stroke="#14549a" stroke-width="1.5"/><rect x="1" y="2" width="12" height="3" fill="#14549a"/></svg><span>SEP 20<sup>TH.</sup> 2022</span></div>
        <h3 class="card-title">Contrary to popular belief, Lorem<br>Ipsum is not simply</h3>
        <div class="card-rule"></div>
        <p class="card-text">There are many variations of passages of<br>Lorem Ipsum available, but the majority have care<br>suffered alteration in some form...</p>
      </div>
      <a class="read-more">READ MORE</a>
    </article>

    <article class="abs card" style="left:612px">
      <div class="card-photo photo-workouts" role="img" aria-label="Two people doing push-ups on kettlebells in a gym"></div>
      <span class="tag"><svg width="9" height="9" viewBox="0 0 9 9"><path d="M4 0h5v5L4 9 0 5z" fill="#fff"/></svg>WORKOUTS</span>
      <div class="card-body">
        <div class="date"><svg width="13" height="12" viewBox="0 0 14 13"><rect x="1" y="2" width="12" height="10" fill="none" stroke="#14549a" stroke-width="1.5"/><rect x="1" y="2" width="12" height="3" fill="#14549a"/></svg><span>DEC 18<sup>TH.</sup> 2022</span></div>
        <h3 class="card-title">Contrary to popular belief, Lorem<br>Ipsum is not simply</h3>
        <div class="card-rule"></div>
        <p class="card-text">There are many variations of passages of<br>Lorem Ipsum available, but the majority have care<br>suffered alteration in some form...</p>
      </div>
      <a class="read-more">READ MORE</a>
    </article>
  </section>
</main>

<footer class="site-footer">
  <div class="brand footer-brand"><span class="brand-dot"></span>Ride the amber tide</div>
  <nav class="footer-nav">
    <span class="home">Home</span><span>About Us</span><span class="active">Nutrition</span><span>Training</span><span>Workouts</span><span>Forum</span><span>Contact Us</span>
  </nav>
  <span class="footer-rule" style="left:306px"></span>
  <div class="footer-social">
    <span class="dot" aria-label="Social profile link"></span>
    <span class="dot blue" aria-label="Social profile link"></span>
    <span class="dot" aria-label="Social profile link"></span>
  </div>
  <span class="footer-rule" style="left:689px"></span>
  <p class="copyright">© 2022 <span>Ride the amber tide.</span> All Right Reserved.</p>
  <span class="to-top"></span>
  <svg class="to-top-arrow" width="16" height="16" viewBox="0 0 16 16"><path d="M5 9l3-3 3 3M5 12l3-3 3 3" fill="none" stroke="#fff" stroke-width="1.4"/></svg>
</footer>

</body>
</html>
```